Flyer for annual KESTREL SUMMIT 2020

I would like a church event flyer designed. The event is called "KESTREL SUMMIT 2020". I am looking for a professional, yet catchy design that uses our brand colors and logo creatively while communicating key information of the event effectively.

1. The logo is attached in two color formats. The designer has the choice to use them as he/she want.

2. The location of the event is: Harlow Community Center, 239 Fennimore Street, Portland, ME 04117

3. Time and date of event. The designer can organize and format the date and time as he/she pleases.
Thursday December 31st @ 6:30PM
Friday January 1st @ 6:30PM
Saturday 2nd @ 6:30PM
Sunday 3rd @ 4:30PM

4. The topic of the event is "In Fire and On Fire". The designer is free to use this phrase as he/she pleases to create a good composition.

5. Speaker: Prophet Marcus Olunde (2 pictures of the speaker to choose from are attached)

6. Contact information: contact@brightmeadowfold.org - Telephone number: 207 583 2914

7. I would also like the following three words on the flyer. These words describe the focus of the event: FIRE, REVIVAL, PROPHETIC

Target Market(s)

Young adults

Font styles to use
Sans Serif

Requirements
Must have
• Logo, speaker's picture
Should not have
• cross image, church image

```html
<!DOCTYPE html>
<html lang="en">
<head>
<meta charset="utf-8">
<title>Kestrel Summit 2020 Flyer</title>
<link rel="stylesheet" href="https://fonts.googleapis.com/css2?family=Cinzel:wght@400;600;700&display=swap">
<style>
  :root {
    --navy: #062b52;
    --orange: #e98a19;
    --white: #ffffff;
    --page: #e4e4e4;
    --photo-a: #8a7f78;
    --photo-b: #b5402a;
  }
  * { margin: 0; padding: 0; box-sizing: border-box; }
  html, body {
    width: 1070px; height: 1200px; overflow: hidden;
    background: var(--page);
    font-family: "Cinzel", serif;
  }
  .flyer {
    position: absolute; left: 122px; top: 14px;
    width: 825px; height: 1172px;
    background: var(--navy); overflow: hidden;
  }
  .abs { position: absolute; }
  .brand {
    left: 565px; top: 92px; width: 200px; text-align: right;
    color: var(--white); font-size: 54px; font-weight: 400; letter-spacing: 1px; line-height: 1;
  }
  .title { left: 56px; top: 110px; font-weight: 600; line-height: 1; }
  .title span { display: block; }
  .title .t1 { color: var(--orange); font-size: 76px; }
  .title .t2 { color: var(--white); font-size: 80px; margin-top: 10px; }
  .title .t3 { color: var(--orange); font-size: 76px; margin-top: 10px; }
  .venue { left: 62px; top: 388px; display: flex; gap: 16px; color: var(--white); }
  .venue svg { width: 38px; height: 52px; flex: none; }
  .venue p { font-size: 21px; line-height: 31px; letter-spacing: .5px; }
  .schedule { left: 55px; top: 474px; width: 706px; color: var(--white); }
  .schedule .dates {
    display: grid; grid-template-columns: 190px 180px 183px 153px;
    border-top: 2px solid var(--orange); border-bottom: 2px solid var(--orange);
    padding: 7px 0 6px 18px; font-size: 21px; line-height: 26px;
  }
  .schedule .times {
    display: grid; grid-template-columns: 190px 180px 183px 153px;
    padding: 14px 0 0 18px; font-size: 17px; line-height: 25px;
  }
  .feature { left: 0; top: 625px; width: 825px; height: 433px; background: var(--orange); }
  .portrait {
    left: 57px; top: 42px; width: 352px; height: 352px; border-radius: 50%;
    border: 7px solid var(--white);
    background: radial-gradient(circle at 50% 75%, var(--photo-b) 0 30%, var(--photo-a) 62%);
  }
  .label {
    display: inline-block; background: var(--white); color: var(--orange);
    border-radius: 16px; font-size: 25px; line-height: 32px; padding: 0 18px; width: 156px;
  }
  .speaker { left: 442px; top: 71px; }
  .block-text { color: var(--white); font-size: 35px; line-height: 40px; font-weight: 600; margin: 16px 0 0 32px; }
  .topic { left: 442px; top: 237px; }
  .contact {
    left: 0; top: 1058px; width: 825px; height: 36px; background: var(--white);
    color: var(--navy); font-size: 21px; line-height: 36px; text-align: center; font-weight: 600;
  }
  .focus {
    left: 0; top: 1094px; width: 825px; height: 78px; color: var(--white);
    font-size: 37px; line-height: 78px; text-align: center; letter-spacing: 1px;
  }
</style>
</head>
<body>
  <main class="flyer">
    <div class="abs brand">SELVANE</div>

    <h1 class="abs title">
      <span class="t1">KESTREL</span>
      <span class="t2">SUMMIT</span>
      <span class="t3">2020</span>
    </h1>

    <div class="abs venue">
      <svg viewBox="0 0 38 52" aria-hidden="true">
        <path d="M19 1C9 1 1 9 1 19c0 13 18 32 18 32s18-19 18-32C37 9 29 1 19 1z" fill="#fff"/>
        <circle cx="19" cy="18" r="7" fill="#062b52"/>
      </svg>
      <p>Harlow Community Center,<br>239 Fennimore Street, Portland, ME 04117</p>
    </div>

    <section class="abs schedule">
      <div class="dates"><span>DEC 31ST</span><span>JAN 1ST</span><span>JAN 2ND</span><span>JAN 3RD</span></div>
      <div class="times">
        <span>Thursday<br>@ 6:30PM</span>
        <span>FRIDAY<br>@ 6:30PM</span>
        <span>SATURDAY<br>@ 6:30PM</span>
        <span>SUNDAY<br>@ 4:30PM</span>
      </div>
    </section>

    <section class="abs feature">
      <div class="abs portrait" role="img" aria-label="Portrait photo of speaker Prophet Marcus Olunde"></div>
      <div class="abs speaker">
        <span class="label">SPEAKER</span>
        <p class="block-text">PROPHET<br>MARCUS OLUNDE</p>
      </div>
      <div class="abs topic">
        <span class="label">TOPIC</span>
        <p class="block-text">IN FIRE<br>AND ON FIRE</p>
      </div>
    </section>

    <p class="abs contact">contact@brightmeadowfold.org - Telephone : 207 583 2914</p>
    <p class="abs focus">FIRE, REVIVAL, PROPHETIC</p>
  </main>
</body>
</html>
```